Amberline Picture Works Web Design

COMPANY: AMBERLINE PICTURE WORKS
LOCATION: SHANGHAI, CHINA
AREA: FILM/TV DRAMA/COMMERCIALS/GAME POST PRODUCTION, SOUND DESIGN, MUSIC, and GAME.
WEB STYLE: SIMPLE, PROFESSIONAL, TRUSTWORTHY

LANGUAGE: ENGLISH, CHINESE. (Same layout, different language)
UPDATE: AFTER PROJECT FINISHED, WE NEED UPDATE BY OURSELVES.

MAIN SUBJECT: 6
1 HOMEPAGE
2 ABOUT US
3 TEAM
4 SERVICES
5 FACILITY
6 CONTACT

add one page of JOB OPPORTUNITIES.

DETAILS
1 HOMEPAGE
SLOGAN: Amberline Picture Works provides a well-designed working environment which amplifies your team’s ability to reach their creative goals.

Our services include:
 Feature Films
 Music & Scoring
 Commercials
 ADR & Foley
 Sound & Picture Editorial
 Sound Design
 Video Game

2 ABOUT US
Amberline Picture Works is located in the premiere South-Bund area of Shanghai. Occupying a 5000 square meter Technical Building, Amberline Picture Works was built by a filmmaker for filmmakers, and is one of the largest, most versatile full-service post-production facilities in China.

Amberline Picture Works is positioning to be at the forefront of the latest technology. Our goal is to provide a comprehensive solution for the post-production needs of our clients. We offer two fully-equipped dubbing stages (one of which will be certified VORTAN SPHERA ELITE), a large variety of both picture and sound editing rooms, impressive Foley and ADR stages, a world-class scoring stage, and complete audio and video transfer services.

We can handle your entire project from editing all the way to the end of the final sound mix; all under one extremely comfortable roof. We fully realize that the true art is in listening to the needs of our clients and making their greatest vision a reality. To this end our creative team's expertise, with a network of sound supervisors, editors and mixers, will deliver the magic you need. Producers and directors will also find our richly appointed guest accommodations to be a comfortable and soothing place to wind up the day. Every aspect of your project will be taken care of by a skilled and dedicated team, in the way that is best suited to you.

3 TEAM
(attachment 01)

4 SERVICES
Sound Mix
ADR
FOLEY
MUSIC
Sound Design
Sound Edit
Picture Edit
for all the Films, TV Drama, Commercials, Video Games, Online Media
(attachment 02, use photo)

5 FACILITY
(attachment 03)

6 CONTACT
(attachment04)
with map

Reason: Designers work are great, my bosses will spend 1-2 days select one of these web design, and spend 1-2 days to make some change, maybe use new photos.

```html
<!DOCTYPE html>
<html lang="en">
<head>
<meta charset="utf-8">
<title>Amberline Picture Works</title>
<link href="https://fonts.googleapis.com/css2?family=Mulish:wght@300;400;600;700;800&family=PT+Sans:ital,wght@0,400;0,700;1,400&display=swap" rel="stylesheet">
<style>
:root{
  --navy:#2b3a6b;
  --navy-dark:#22305a;
  --accent:#3a5aa0;
  --text:#333;
  --muted:#8a8a8a;
  --line:#e2e2e2;
  --grey-bg:#f1f1f1;
  --footer:#363638;
  --footer-bottom:#2b2b2d;
  --footer-text:#cfcfcf;
  --footer-muted:#9a9a9a;
}
*{margin:0;padding:0;box-sizing:border-box}
html,body{width:1200px;height:2356px;overflow:hidden}
body{font-family:"Mulish",Arial,sans-serif;color:var(--text);background:#fff;position:relative}
.abs{position:absolute}

/* top bar */
.topbar{left:0;top:0;width:1200px;height:31px;background:var(--navy)}
.topbar .contact{left:110px;top:0;height:31px;display:flex;align-items:center;gap:26px;color:#fff;font-size:11px}
.topbar .contact span{display:flex;align-items:center;gap:8px}
.topbar .social{right:110px;top:6px;display:flex;gap:8px}
.topbar .social i{width:19px;height:19px;border-radius:50%;background:#dfe3ee;display:block}

/* header */
.header{left:0;top:31px;width:1200px;height:117px;background:#fff;border-bottom:1px solid #eee}
.logo{left:112px;top:20px;width:118px}
.logo .name{font-weight:800;font-size:22px;color:var(--navy);letter-spacing:0.5px;line-height:1;text-transform:uppercase}
.logo .name small{display:block;font-size:11px;font-weight:700;letter-spacing:1.5px;margin-top:3px}
.logo .sub{margin-top:7px;border-top:1px solid #999;padding-top:4px;font-size:11px;color:#777;letter-spacing:1.5px;text-transform:uppercase}
.nav{left:416px;top:46px;display:flex;gap:34px;font-size:14px;color:#333}
.nav a{color:inherit;text-decoration:none;display:flex;align-items:center;gap:7px;padding-bottom:10px}
.nav a.active{color:var(--navy);border-bottom:2px solid var(--navy)}
.search{left:1068px;top:44px}

/* hero */
.hero{left:0;top:148px;width:1200px;height:369px;background:radial-gradient(circle at 20% 30%,#5a6a55 0,#2a2a28 35%,#141414 70%),#1a1a1a}
.hero .glow{left:0;top:0;width:1200px;height:369px;background:linear-gradient(100deg,rgba(90,180,150,.25) 0,rgba(30,30,30,0) 35%,rgba(200,170,60,.18) 60%,rgba(80,110,230,.25) 100%)}
.slogan{left:110px;top:117px;width:980px;height:96px;background:rgba(235,235,238,.9);display:flex;align-items:center;justify-content:center;text-align:center;font-size:22px;line-height:35px;color:#333}
.slogan b{color:var(--navy);font-weight:800}

/* services */
.services-title{left:112px;top:552px;font-size:23px;font-weight:400;color:#333}
.services-intro{left:112px;top:620px;width:215px;font-size:11.5px;line-height:24px;color:#888}
.service{width:181px;text-align:center}
.service .icon{width:50px;height:50px;background:var(--navy);margin:23px auto 0;display:flex;align-items:center;justify-content:center}
.service h3{font-size:17px;font-weight:400;margin-top:20px;color:#333}
.service p{font-size:11.5px;line-height:18px;color:#8a8a8a;margin:11px 14px 0}
.vline{width:1px;background:var(--line)}
.hline{height:1px;background:var(--line)}

/* portfolio */
.portfolio{left:0;top:1040px;width:1200px;height:504px;background:var(--grey-bg)}
.section-title{width:1200px;text-align:center;font-size:29px;font-weight:300;color:#333;left:0}
.section-sub{width:1200px;text-align:center;font-size:16px;letter-spacing:.3px;color:#333;left:0;text-transform:uppercase}
.portfolio p.lead{left:150px;width:900px;top:118px;text-align:center;font-size:13px;line-height:24px;color:#8a8a8a}
.shot{top:200px;width:245px;height:233px}
.caption{left:0;bottom:0;width:245px;height:82px;background:#000;color:#fff;text-align:center}
.caption .t{font-size:13px;margin-top:14px;letter-spacing:.3px}
.caption .s{font-size:11.5px;margin-top:14px}
.tools{left:47px;top:98px;display:flex;gap:18px}
.tools span{width:40px;height:40px;border-radius:50%;background:var(--navy);display:flex;align-items:center;justify-content:center}
.arrow{top:297px}

/* clients */
.testimonial{left:116px;top:1691px;width:466px;height:154px;background:#f1f1f1}
.testimonial p{left:17px;top:22px;width:430px;font-size:11px;line-height:18px;color:#999}
.avatar{left:17px;top:91px;width:40px;height:40px;border-radius:50%;background:linear-gradient(135deg,#6b5b55,#222)}
.who{left:73px;top:94px}
.who b{display:block;font-size:12.5px;font-weight:400;color:#333}
.who span{display:block;font-size:10px;color:var(--accent);margin-top:7px}
.dots{left:326px;top:1853px;font-size:14px;color:#888;letter-spacing:2px}
.client{width:163px;height:70px;display:flex;align-items:center;justify-content:center;gap:8px;font-size:18px;font-weight:700;color:#333}
.client i{width:22px;height:22px;border-radius:50%;background:#333;display:block}

/* footer */
.footer{left:0;top:1922px;width:1200px;height:374px;background:var(--footer)}
.fcol h4{font-size:12px;font-weight:700;color:#fff;letter-spacing:.3px;font-family:"PT Sans",sans-serif}
.fcol{top:45px;font-family:"PT Sans",sans-serif}
.about-text{margin-top:23px;width:195px;font-size:12px;line-height:20px;font-style:italic;color:var(--footer-muted)}
.posts{margin-top:18px;width:218px;list-style:none}
.posts li{font-size:12px;color:#ddd;padding:10px 0 9px;border-bottom:1px solid #454548}
.tweet{width:215px;font-size:12px;line-height:20px;color:var(--footer-muted);padding:10px 0 12px;border-bottom:1px solid #454548}
.tweet b{color:#fff;font-weight:400}
.tweet em{font-style:normal;color:#eee}
.info{margin-top:23px;font-size:11.5px;line-height:19px;color:#ccc}
.info div{display:flex;align-items:center;gap:10px;margin-top:14px}
.bottom{left:0;top:2296px;width:1200px;height:60px;background:var(--footer-bottom);border-top:1px solid #444}
.bottom .copy{left:110px;top:24px;font-size:11px;color:#bbb;font-family:"PT Sans",sans-serif}
.bottom .social{left:924px;top:24px;display:flex;gap:22px}
.bottom .social i{width:13px;height:13px;border-radius:50%;background:#666;display:block}
.tip{left:907px;top:2282px;background:#444;color:#ddd;font-size:10px;padding:2px 7px;font-family:"PT Sans",sans-serif}
</style>
</head>
<body>

<div class="abs topbar">
  <div class="abs contact">
    <span><svg width="12" height="9" viewBox="0 0 12 9"><rect width="12" height="9" fill="#fff"/><path d="M0 0l6 5 6-5" stroke="#2b3a6b" fill="none"/></svg>info@amberlinepw.com</span>
    <span><svg width="10" height="10" viewBox="0 0 10 10"><path d="M2 0l2 2.5-1.2 1.3a6 6 0 003.4 3.4L7.5 6 10 8l-1.5 2C4 10 0 6 0 1.5z" fill="#fff"/></svg>86 21 5550-0148</span>
  </div>
  <div class="abs social"><i></i><i></i><i></i><i></i></div>
</div>

<header class="abs header">
  <div class="abs logo">
    <div class="name">Amberline<small>Picture Works</small></div>
    <div class="sub">Post Studio</div>
  </div>
  <nav class="abs nav">
    <a class="active"><svg width="13" height="12" viewBox="0 0 13 12"><path d="M6.5 0L0 6h2v6h3.5V8h2v4H11V6h2z" fill="currentColor"/></svg>HOME</a>
    <a><svg width="12" height="12" viewBox="0 0 12 12"><circle cx="6" cy="6" r="5" fill="none" stroke="currentColor" stroke-width="1.5"/><rect x="5.3" y="5" width="1.4" height="4" fill="currentColor"/></svg>ABOUT US</a>
    <a><svg width="17" height="12" viewBox="0 0 17 12"><circle cx="8.5" cy="3" r="3" fill="currentColor"/><circle cx="3" cy="4" r="2" fill="currentColor"/><circle cx="14" cy="4" r="2" fill="currentColor"/><path d="M3 12a5.5 5 0 0111 0zM0 10a3 3 0 015 0zM12 10a3 3 0 015 0z" fill="currentColor"/></svg>TEAM</a>
    <a><svg width="13" height="12" viewBox="0 0 13 12"><circle cx="4" cy="8" r="3" fill="none" stroke="currentColor" stroke-width="1.6"/><circle cx="10" cy="3" r="2" fill="none" stroke="currentColor" stroke-width="1.4"/></svg>SERVICES</a>
    <a><svg width="12" height="12" viewBox="0 0 12 12"><path d="M6 0l1.3 3.7L11 5 7.3 6.3 6 12 4.7 6.3 1 5l3.7-1.3z" fill="currentColor"/></svg>FACILITY</a>
    <a><svg width="14" height="11" viewBox="0 0 14 11"><rect width="14" height="11" fill="currentColor"/><path d="M0 0l7 6 7-6" stroke="#fff" fill="none"/></svg>CONTACT</a>
  </nav>
  <svg class="abs search" width="20" height="20" viewBox="0 0 20 20"><circle cx="8" cy="8" r="6" fill="none" stroke="#333" stroke-width="2.6"/><path d="M12.5 12.5l6 6" stroke="#333" stroke-width="3"/></svg>
</header>

<section class="abs hero" role="img" aria-label="Close-up of a lit audio mixing console with rows of glowing knobs">
  <div class="abs glow"></div>
  <div class="abs slogan"><div><b>AMBERLINE PICTURE WORKS</b> Provides a <b>WELL-DESIGNED</b> Working Environment Which<br><b>AMPLIFIES</b> Your Team’s <b>ABILITY</b> to Reach Their <b>CREATIVE GOALS</b></div></div>
</section>

<h2 class="abs services-title">Our Services</h2>
<p class="abs services-intro">Lorem ipsum dolor sit amet, consectetuer adipiscing elit, sed diam nonummy nibh euismod tincidunt ut laoreet dolore magna aliquam erat volutpat. Ut wisi enim ad minim veniam, quis nostrud exerci tation ullamcorper suscipit lobortis nisl ut aliquip ex soluta nobis eleifend option congue nihil imperdiet doming id quod mazim ea commodo consequat. Duis autem vel eum iriure dolor in hendrerit in vulputate velit esse soluta nobis eleifend option congue nihil imperdiet doming id quod mazim assum.</p>

<div class="abs vline" style="left:356px;top:555px;height:435px"></div>
<div class="abs vline" style="left:551px;top:555px;height:195px"></div>
<div class="abs vline" style="left:737px;top:555px;height:195px"></div>
<div class="abs vline" style="left:918px;top:555px;height:195px"></div>
<div class="abs vline" style="left:551px;top:797px;height:193px"></div>
<div class="abs vline" style="left:737px;top:797px;height:193px"></div>
<div class="abs vline" style="left:918px;top:797px;height:193px"></div>
<div class="abs hline" style="left:378px;top:768px;width:160px"></div>
<div class="abs hline" style="left:566px;top:768px;width:158px"></div>
<div class="abs hline" style="left:750px;top:768px;width:158px"></div>
<div class="abs hline" style="left:930px;top:768px;width:158px"></div>

<div class="abs service" style="left:371px;top:555px"><div class="icon"><svg width="28" height="28" viewBox="0 0 28 28"><g fill="none" stroke="#fff" stroke-width="2"><circle cx="14" cy="14" r="4"/><circle cx="14" cy="6" r="4"/><circle cx="21.5" cy="11.5" r="4"/><circle cx="18.5" cy="20.5" r="4"/><circle cx="9.5" cy="20.5" r="4"/><circle cx="6.5" cy="11.5" r="4"/></g></svg></div><h3>Feature Films</h3><p>Lorem ipsum dolor sit amet, consectetuer adipiscing elit, sed diam</p></div>
<div class="abs service" style="left:553px;top:555px"><div class="icon"><svg width="24" height="26" viewBox="0 0 24 26"><path d="M8 4l14-4v18" fill="none" stroke="#fff" stroke-width="2.4"/><path d="M8 4v18" stroke="#fff" stroke-width="2.4"/><ellipse cx="5" cy="22" rx="4" ry="3" fill="#fff"/><ellipse cx="19" cy="18" rx="4" ry="3" fill="#fff"/></svg></div><h3>Music &amp; Scoring</h3><p>Lorem ipsum dolor sit amet, consectetuer adipiscing elit, sed diam</p></div>
<div class="abs service" style="left:733px;top:555px"><div class="icon"><svg width="28" height="26" viewBox="0 0 28 26"><path d="M1 1v24h26" fill="none" stroke="#fff" stroke-width="2"/><rect x="5" y="10" width="3" height="13" fill="#fff"/><rect x="10" y="4" width="3" height="19" fill="#fff"/><rect x="15" y="12" width="3" height="11" fill="#fff"/><rect x="20" y="7" width="3" height="16" fill="#fff"/></svg></div><h3>Commercials</h3><p>Lorem ipsum dolor sit amet, consectetuer adipiscing elit, sed diam</p></div>
<div class="abs service" style="left:914px;top:555px"><div class="icon"><svg width="20" height="30" viewBox="0 0 20 30"><rect x="5" y="0" width="10" height="18" rx="5" fill="#fff"/><path d="M1 13a9 9 0 0018 0M10 22v6M5 29h10" fill="none" stroke="#fff" stroke-width="2"/></svg></div><h3>ADR &amp; Foley</h3><p>Lorem ipsum dolor sit amet, consectetuer adipiscing elit, sed diam</p></div>

<div class="abs service" style="left:371px;top:797px"><div class="icon"><svg width="26" height="30" viewBox="0 0 26 30"><g stroke="#fff" stroke-width="2"><path d="M4 0v30M13 0v30M22 0v30"/></g><rect x="0" y="18" width="8" height="4" fill="#fff"/><rect x="9" y="7" width="8" height="4" fill="#fff"/><rect x="18" y="14" width="8" height="4" fill="#fff"/></svg></div><h3>Sound Mix</h3><p>Lorem ipsum dolor sit amet, consectetuer adipiscing elit, sed diam</p></div>
<div class="abs service" style="left:553px;top:797px"><div class="icon"><svg width="28" height="28" viewBox="0 0 28 28"><rect x="2" y="4" width="22" height="22" rx="3" fill="none" stroke="#fff" stroke-width="2.4"/><path d="M11 17l2-5 12-12 3 3-12 12z" fill="#fff"/></svg></div><h3>Picture Edit</h3><p>Lorem ipsum dolor sit amet, consectetuer adipiscing elit, sed diam</p></div>
<div class="abs service" style="left:733px;top:797px"><div class="icon"><svg width="34" height="24" viewBox="0 0 34 24"><path d="M0 12h5l2-5 3 12 3-18 3 22 3-17 3 13 3-9 2 4h7" fill="none" stroke="#fff" stroke-width="2"/></svg></div><h3>Sound Design</h3><p>Lorem ipsum dolor sit amet, consectetuer adipiscing elit, sed diam</p></div>
<div class="abs service" style="left:914px;top:797px"><div class="icon"><svg width="30" height="30" viewBox="0 0 30 30"><circle cx="15" cy="15" r="10" fill="none" stroke="#fff" stroke-width="2.4"/><circle cx="15" cy="15" r="4" fill="#fff"/><path d="M15 0v6M15 24v6M0 15h6M24 15h6" stroke="#fff" stroke-width="2.4"/></svg></div><h3>Video Game</h3><p>Lorem ipsum dolor sit amet, consectetuer adipiscing elit, sed diam</p></div>

<section class="abs portfolio">
  <h2 class="abs section-title" style="top:40px">Our Portfolio</h2>
  <div class="abs section-sub" style="top:85px">Best &amp; Most Popular of Our Works</div>
  <p class="abs lead">Lorem ipsum dolor sit amet, consectetuer adipiscing elit, sed diam nonummy nibh euismod tincidunt ut laoreet dolore magna aliquam erat volutpat. Ut wisi enim ad minim veniam, quis nostrud exerci tation ullamcorper suscipit lobortis nisl ut aliquip ex ea commodo consequat.</p>
  <div class="abs shot" style="left:110px;background:linear-gradient(160deg,#8a6a4a,#4b3a2c)" role="img" aria-label="Engineer working at a mixing desk in a studio"></div>
  <div class="abs shot" style="left:355px;background:linear-gradient(160deg,#a8a59e,#5e5b55)" role="img" aria-label="Mixing console faders in a control room">
    <div class="abs tools">
      <span><svg width="14" height="16" viewBox="0 0 14 16"><path d="M0 0h9l5 5v11H0z" fill="#fff"/><path d="M3 8h8M3 11h8" stroke="#2b3a6b"/></svg></span>
      <span><svg width="16" height="16" viewBox="0 0 16 16"><g fill="none" stroke="#fff" stroke-width="2.2"><rect x="1" y="7" width="8" height="5" rx="2.5" transform="rotate(-45 5 9.5)"/><rect x="7" y="4" width="8" height="5" rx="2.5" transform="rotate(-45 11 6.5)"/></g></svg></span>
      <span><svg width="16" height="16" viewBox="0 0 16 16"><circle cx="6.5" cy="6.5" r="5" fill="none" stroke="#fff" stroke-width="2"/><path d="M10 10l5 5M4 6.5h5M6.5 4v5" stroke="#fff" stroke-width="2"/></svg></span>
    </div>
    <div class="abs caption"><div class="t">LOREM IPSUM DOLOR SIT</div><div class="s">Amet adicsing consectetuer</div></div>
  </div>
  <div class="abs shot" style="left:600px;background:linear-gradient(180deg,#3a2220,#6a1e22 40%,#8a7a6e)" role="img" aria-label="Screening room with a large projection screen"></div>
  <div class="abs shot" style="left:845px;background:linear-gradient(120deg,#b89a72,#3a3028 55%,#151515)" role="img" aria-label="Close-up of studio monitor speakers"></div>
  <svg class="abs arrow" style="left:120px" width="16" height="30" viewBox="0 0 16 30"><path d="M14 2L2 15l12 13" fill="none" stroke="#fff" stroke-width="3"/></svg>
  <svg class="abs arrow" style="left:1062px" width="16" height="30" viewBox="0 0 16 30"><path d="M2 2l12 13L2 28" fill="none" stroke="#fff" stroke-width="3"/></svg>
</section>

<h2 class="abs section-title" style="top:1585px">Clients &amp; Testimonials</h2>
<div class="abs section-sub" style="top:1631px">More then 20 000 of happy customers</div>

<div class="abs testimonial">
  <p class="abs">Vivamus lectus eget mollis ligula. Vesti bulum vitae ultrices justo. Donec sed venenatis lacus. Lorem viverra, augue nec pellen tesque sagittis, quam tortor suscipit elit lectus eget mollis ligula nostra mattis nulla eleifend bulum vitae.</p>
  <div class="abs avatar" role="img" aria-label="Customer portrait"></div>
  <div class="abs who"><b>Daniel Morrow</b><span>happy customer</span></div>
</div>
<div class="abs dots">• • • • •</div>

<div class="abs vline" style="left:764px;top:1696px;height:64px"></div>
<div class="abs vline" style="left:931px;top:1696px;height:64px"></div>
<div class="abs vline" style="left:764px;top:1785px;height:64px"></div>
<div class="abs vline" style="left:931px;top:1785px;height:64px"></div>
<div class="abs hline" style="left:606px;top:1773px;width:480px"></div>
<div class="abs client" style="left:600px;top:1693px"><i></i>Paloma</div>
<div class="abs client" style="left:767px;top:1693px"><i></i>Quillbase</div>
<div class="abs client" style="left:934px;top:1693px">Cartwell</div>
<div class="abs client" style="left:600px;top:1782px"><i></i>Tasklane</div>
<div class="abs client" style="left:767px;top:1782px"><i></i>Hoopstudio</div>
<div class="abs client" style="left:934px;top:1782px">Selecta</div>

<footer class="abs footer">
  <div class="abs fcol" style="left:132px"><h4>ABOUT US</h4>
    <p class="about-text">Lorem ipsum ex vix illud nonummy, novum tation et his. At vix scriptaset patrioque scribentur, at pro fugit erts verterem molestiae, sed et vivendo ali Lorem ipsum ex vix illud nonummy, novum tation et his. At vix scripta patrioque scribentur.. sed et vivendo ali Lorem ipsum ex vix illud nonummy, novum tation et his. At vix scripta patrioque scribentur...</p></div>
  <div class="abs fcol" style="left:372px"><h4>RECENT POSTS</h4>
    <ul class="posts"><li>Voluptas Sadips Ipsums Dolors Untra</li><li>Fugiats Litora Ultrices Ante Auctor</li><li>Sapien Litora Dolores Ultrices</li><li>Nemis Fugiats Voluptas Dolores Uns</li><li>Fugiats Litora Ultrices Ante Auctor</li></ul></div>
  <div class="abs fcol" style="left:612px"><h4>TWITTER</h4>
    <div style="margin-top:12px">
      <div class="tweet"><b>@velora</b> I What an aweosme theme! We love it, tons of options and great design, thank you! :) <em>12 minutes ago</em></div>
      <div class="tweet"><b>@velora</b> you've got to check this one out, very cool looking! <em>25 minutes ago</em></div>
      <div class="tweet" style="border:0"><b>@velora</b> I What an aweosme theme! We love it, tons of options and great design, thank you! :) <em>12 minutes ago</em></div>
    </div></div>
  <div class="abs fcol" style="left:891px"><h4>CONTACT US</h4>
    <div class="info">中国上海黄浦区兰溪路48号<br>No.48 Lanxi Rd.<br>Shanghai China, 200000
      <div><svg width="11" height="11" viewBox="0 0 10 10"><path d="M2 0l2 2.5-1.2 1.3a6 6 0 003.4 3.4L7.5 6 10 8l-1.5 2C4 10 0 6 0 1.5z" fill="#bbb"/></svg>86 21 5550-0148</div>
      <div><svg width="13" height="10" viewBox="0 0 13 10"><rect width="13" height="10" fill="none" stroke="#bbb" stroke-width="2"/><path d="M3 4h7M3 6h7" stroke="#bbb"/></svg>www.amberlinepw.com</div>
      <div><svg width="13" height="10" viewBox="0 0 13 10"><rect width="13" height="10" fill="#bbb"/><path d="M0 0l6.5 5L13 0" stroke="#363638" fill="none"/></svg>info@amberlinepw.com</div>
    </div></div>
</footer>

<div class="abs bottom">
  <div class="abs copy">copyright© 2014 Amberline Picture Works. All Rights Reserved</div>
  <div class="abs social"><i></i><i></i><i></i><i></i><i></i></div>
</div>
<div class="abs tip">Follow us</div>

</body>
</html>
```